IT Company based on Biology Business Needs a Business Card Design

We need a business card design for a new company called 'Lumen CELL'. We develop the machine learning solutions especially focused on deep learning algorithms for biology industry. Our initial product is a vision detection on biological images to help doctors diagnose the symptoms. We would like to see designs that use the color green.

Industry/Entity Type

Business

```html
<!DOCTYPE html>
<html lang="en">
<head>
<meta charset="utf-8">
<title>Lumen CELL — Business Card</title>
<link rel="stylesheet" href="https://fonts.googleapis.com/css2?family=Open+Sans:wght@400;600;700&display=swap">
<style>
  :root {
    --page-bg: #e4e2de;
    --card-bg: #f3f4f2;
    --green-light: #62ad43;
    --green-mid: #4a9a36;
    --green-dark: #1b6a37;
    --brand-green: #4ea33e;
    --name-green: #3d7a48;
    --title-green: #6aa452;
    --contact-green: #5f9f4a;
    --web-green: #2f6b45;
    --band-white: #fbfcfb;
  }
  * { margin: 0; padding: 0; box-sizing: border-box; }
  html, body {
    width: 1200px; height: 970px; overflow: hidden;
    background: var(--page-bg);
    font-family: "Open Sans", Arial, sans-serif;
  }
  .business-card {
    position: absolute; left: 80px; top: 189px;
    width: 1040px; height: 592px;
    background: var(--card-bg);
    overflow: hidden;
    box-shadow: 0 6px 24px rgba(0,0,0,0.15);
  }
  .card-swoosh { position: absolute; inset: 0; width: 100%; height: 100%; }
  .brand {
    position: absolute; left: 62px; top: 120px;
    display: flex; align-items: center; gap: 22px;
  }
  .brand-dot {
    width: 58px; height: 58px; border-radius: 50%;
    background: var(--brand-green);
  }
  .brand-name {
    font-weight: 600; font-size: 74px; letter-spacing: -2px;
    color: var(--brand-green); line-height: 1;
  }
  .person { position: absolute; left: 62px; top: 335px; }
  .person-name {
    font-weight: 700; font-size: 31px; color: var(--name-green);
    letter-spacing: 0.5px; line-height: 1.1;
  }
  .person-title {
    font-weight: 400; font-size: 26px; color: var(--title-green); line-height: 1.15;
  }
  .contacts { position: absolute; left: 66px; top: 422px; list-style: none; }
  .contact-item {
    display: flex; align-items: center; gap: 10px;
    font-size: 26px; color: var(--contact-green); height: 34px;
  }
  .contact-icon {
    width: 27px; height: 27px; background: var(--name-green);
    display: flex; align-items: center; justify-content: center;
  }
  .website {
    position: absolute; left: 66px; top: 510px;
    font-size: 24px; font-weight: 600; color: var(--web-green);
  }
</style>
</head>
<body>
  <div class="business-card">
    <svg class="card-swoosh" viewBox="0 0 1040 592" aria-hidden="true">
      <defs>
        <linearGradient id="panelGreen" x1="0" y1="0" x2="1" y2="1">
          <stop offset="0" stop-color="var(--green-mid)"/>
          <stop offset="0.6" stop-color="var(--green-light)"/>
          <stop offset="1" stop-color="var(--green-mid)"/>
        </linearGradient>
      </defs>
      <path d="M640,0 L1040,0 L1040,592 L790,592 C1120,330 960,80 640,0 Z" fill="url(#panelGreen)"/>
      <path d="M375,0 C760,60 1100,300 745,592" fill="none" stroke="var(--green-dark)" stroke-width="11"/>
    </svg>

    <div class="brand">
      <span class="brand-dot"></span>
      <span class="brand-name">Lumen CELL</span>
    </div>

    <div class="person">
      <p class="person-name">EMPLOYEE NAME</p>
      <p class="person-title">Managing Director</p>
    </div>

    <ul class="contacts">
      <li class="contact-item">
        <span class="contact-icon">
          <svg width="17" height="17" viewBox="0 0 24 24"><path d="M6.6 10.8a15 15 0 0 0 6.6 6.6l2.2-2.2a1 1 0 0 1 1-.25 11.4 11.4 0 0 0 3.6.57 1 1 0 0 1 1 1V20a1 1 0 0 1-1 1A17 17 0 0 1 3 4a1 1 0 0 1 1-1h3.5a1 1 0 0 1 1 1c0 1.25.2 2.45.57 3.57a1 1 0 0 1-.25 1z" fill="#fff"/></svg>
        </span>
        000-111-0000
      </li>
      <li class="contact-item">
        <span class="contact-icon">
          <svg width="18" height="14" viewBox="0 0 18 14"><rect x="1" y="1" width="16" height="12" fill="none" stroke="#fff" stroke-width="1.6"/><path d="M1 1 L9 8 L17 1" fill="none" stroke="#fff" stroke-width="1.6"/></svg>
        </span>
        hello@lumencell.example
      </li>
    </ul>

    <p class="website">www.lumencell.example</p>
  </div>
</body>
</html>
```